Business Card Design

I need a business card for company that is a limited company that was originally an off-road vehicle company (atv's side by sides snowmobiles and motorcycles) and I have recently sold the assets of the company that was operating under a different name and have become semi retired. I continue to do maintenance on these types of vehicles and also sell and install parts and accessories. Recently I have also contracted to a snowmobile club to operate their groomer to groom the snowmobile trails. I would like bright and bold colors.
Industry/Entity Type
Club
Contact Information for Business Card
KTV Holdings Ltd.
Milo Fenwick
780-413-2769

```html
<!DOCTYPE html>
<html lang="en">
<head>
<meta charset="utf-8">
<title>KTV Holdings Ltd. — Business Card</title>
<link href="https://fonts.googleapis.com/css2?family=Open+Sans:wght@300;400;600;700&display=swap" rel="stylesheet">
<style>
  :root {
    --canvas-bg: #e9ebee;
    --card-white: #ffffff;
    --card-edge: #f2f3f5;
    --brand-blue: #1f9be3;
    --brand-blue-light: #3fb0ee;
    --brand-blue-deep: #178bd6;
    --ink: #1d1d1f;
    --ink-soft: #4a4a4e;
    --on-blue: #ffffff;
  }
  * { box-sizing: border-box; margin: 0; padding: 0; }
  html, body { width: 1200px; height: 900px; overflow: hidden; }
  body {
    background: var(--canvas-bg);
    font-family: "Open Sans", Arial, sans-serif;
    position: relative;
  }
  .card {
    position: absolute;
    width: 640px;
    height: 366px;
    background: var(--card-white);
    box-shadow: 0 6px 18px rgba(0,0,0,0.18);
    overflow: hidden;
  }

  /* Front: contact side */
  .card-front { left: 110px; top: 80px; }
  .contact-panel {
    position: absolute;
    left: 0; top: 42px;
    width: 462px; height: 238px;
    background: linear-gradient(100deg, var(--brand-blue-deep), var(--brand-blue-light));
    border-radius: 0 28px 28px 0;
    color: var(--on-blue);
    padding: 62px 0 0 54px;
  }
  .person-first {
    font-weight: 700;
    font-size: 32px;
    letter-spacing: 4px;
    line-height: 1;
  }
  .person-last {
    font-weight: 300;
    font-size: 32px;
    letter-spacing: 4px;
    line-height: 1.05;
    margin-bottom: 16px;
  }
  .contact-line {
    font-weight: 600;
    font-size: 19px;
    line-height: 1.3;
    letter-spacing: 0.3px;
  }
  .credentials {
    position: absolute;
    left: 486px; top: 40px;
    height: 250px;
    writing-mode: vertical-rl;
    transform: rotate(180deg);
    display: flex;
    flex-direction: column;
    justify-content: flex-start;
  }
  .credential-title {
    font-weight: 700;
    font-size: 17px;
    letter-spacing: 3px;
    color: var(--ink);
    line-height: 1.25;
  }
  .credential-line {
    font-weight: 400;
    font-size: 11px;
    color: var(--ink-soft);
    line-height: 1.35;
  }

  /* Back: company side */
  .card-back { left: 450px; top: 474px; }
  .band { position: absolute; left: 0; width: 100%; }
  .band-top { top: 0; height: 20px; background: linear-gradient(90deg, var(--brand-blue-deep), var(--brand-blue-light)); }
  .band-rule { top: 228px; height: 14px; background: var(--brand-blue); }
  .band-base { top: 262px; height: 84px; background: linear-gradient(90deg, var(--brand-blue-deep), var(--brand-blue-light)); }
  .company-name {
    position: absolute;
    left: 0; top: 92px;
    width: 100%;
    text-align: center;
    font-weight: 700;
    font-size: 50px;
    letter-spacing: 2px;
    color: var(--ink);
  }
</style>
</head>
<body>
  <section class="card card-front" aria-label="Business card front">
    <div class="contact-panel">
      <p class="person-first">Milo</p>
      <p class="person-last">Fenwick</p>
      <p class="contact-line">780-413-2769</p>
      <p class="contact-line">ktvhold.77@mailbox.com</p>
    </div>
    <div class="credentials">
      <p class="credential-title">JOURNEYMAN</p>
      <p class="credential-line">Red Seal Small Engine Tech</p>
      <p class="credential-line">Red Seal Heavy Equipment</p>
    </div>
  </section>

  <section class="card card-back" aria-label="Business card back">
    <div class="band band-top"></div>
    <p class="company-name">KTV Holdings Ltd.</p>
    <div class="band band-rule"></div>
    <div class="band band-base"></div>
  </section>
</body>
</html>
```